Glimmerline Showband - presents Modern Hits with a Retro Twist. Needs a poster

We need a poster for a show band called Glimmerline Showband that does modern hits with a retro twist. It's an 8 piece band - 3 female singers, guitar, drums, bass, saxophone, keyboards. The target audiences: wineries, corporate, weddings etc. We want a poster that conveys both the modern and retro aspects of our work. (It's important that you view Copperleaf Parlour on ClipHaven to get a sense of what this style of music is) I have copied in a poster from Artboard Hive _ Velvet Carousel -that we really like.

Target Market(s)

High class - wineries, casinos, up market supper clubs, big weddings, corporate events

Requirements
Must have
• Upper left says something like "Harriet Quellwood Presents":
Nice to have
• I have copied in a poster from Artboard Hive _ Velvet Carousel -that we really like. We like the 3 women on the rocket - quirky, fun and a bit risqué.
Should not have
• Not as much wording as on the Velvet Carousel. It's not a poster for a specific gig but a generic poster for general use. We do not want photos in the bottom left, only names. We will provide.

```html
<!DOCTYPE html>
<html lang="en">
<head>
<meta charset="UTF-8">
<title>Glimmerline Showband Poster</title>
<link rel="stylesheet" href="https://fonts.googleapis.com/css2?family=Bebas+Neue&family=Montserrat:wght@300;400;700;800&family=Cabin:wght@500&display=swap">
<style>
  :root {
    --gold-light: #f8e6ae;
    --gold-mid: #efcf7e;
    --gold-edge: #deac52;
    --red: #e41f26;
    --rule: #e8562f;
    --ink: #1d1b19;
    --photo-warm: #e9c9a0;
    --photo-cool: #b9c4da;
    --photo-rose: #d9707e;
  }
  * { margin: 0; padding: 0; box-sizing: border-box; }
  html, body { width: 900px; height: 1200px; overflow: hidden; }
  body { background: var(--gold-edge); }
  .poster {
    position: relative;
    width: 900px;
    height: 1200px;
    background:
      radial-gradient(ellipse 60% 55% at 50% 45%, var(--gold-light) 0%, var(--gold-mid) 55%, var(--gold-edge) 100%);
    font-family: "Montserrat", sans-serif;
    color: var(--ink);
    text-align: center;
  }
  .presenter {
    position: absolute; top: 78px; left: 0; width: 100%;
    font-family: "Bebas Neue", sans-serif;
    font-size: 86px; line-height: 1;
    color: var(--red);
    letter-spacing: -1px;
    transform: scaleY(1.12);
  }
  .presents {
    position: absolute; top: 166px; left: 0; width: 100%;
    font-weight: 300; font-size: 30px; letter-spacing: 1px;
  }
  .presents-rule {
    position: absolute; top: 204px; left: 396px; width: 108px; height: 4px;
    background: var(--red);
  }
  .band-photo {
    position: absolute; top: 258px; left: 99px; width: 702px; height: 420px;
    background:
      linear-gradient(90deg, var(--photo-warm) 0%, var(--photo-cool) 45%, var(--photo-rose) 80%, rgba(217,112,126,0) 100%);
    opacity: 0.75;
    border-radius: 4px;
  }
  .photo-rule {
    position: absolute; top: 680px; left: 139px; width: 618px; height: 3px;
    background: var(--rule);
  }
  .band-name {
    position: absolute; top: 702px; left: 0; width: 100%;
    font-weight: 800; font-size: 84px; line-height: 1;
    color: var(--red); letter-spacing: 1px;
  }
  .band-type {
    position: absolute; top: 800px; left: 0; width: 100%;
    font-weight: 400; font-size: 84px; line-height: 1;
    letter-spacing: 2px;
  }
  .name-rule {
    position: absolute; top: 904px; left: 126px; width: 648px; height: 3px;
    background: var(--rule);
  }
  .tagline {
    position: absolute; top: 930px; left: 0; width: 100%;
    font-family: "Cabin", sans-serif; font-weight: 500;
    font-size: 26px;
  }
  .event-date {
    position: absolute; top: 990px; left: 0; width: 100%; height: 100px;
  }
  .day {
    position: absolute; left: 138px; top: 0;
    font-family: "Bebas Neue", sans-serif;
    font-size: 118px; line-height: 1; color: var(--red);
  }
  .month-year {
    position: absolute; left: 288px; top: 12px; text-align: left;
    font-weight: 700; line-height: 0.95;
  }
  .month { display: block; font-size: 40px; }
  .year { display: block; font-size: 64px; }
  .divider {
    position: absolute; left: 498px; top: 18px; width: 4px; height: 62px;
    background: var(--red);
  }
  .time {
    position: absolute; left: 548px; top: 14px; text-align: left;
    font-weight: 700; font-size: 38px; line-height: 1.2;
  }
  .website {
    position: absolute; top: 1112px; left: 0; width: 100%;
    font-weight: 700; font-size: 28px; letter-spacing: 3px;
    color: var(--red);
  }
</style>
</head>
<body>
  <main class="poster">
    <h1 class="presenter">Harriet Quellwood</h1>
    <p class="presents">PRESENTS</p>
    <div class="presents-rule"></div>

    <div class="band-photo" role="img" aria-label="Photo of the three female singers in evening gowns with microphones, on a scattered star background"></div>
    <div class="photo-rule"></div>

    <h2 class="band-name">GLIMMERLINE</h2>
    <p class="band-type">SHOWBAND</p>
    <div class="name-rule"></div>

    <p class="tagline">Feoluenig tHe amaging eoval and hamong talents of</p>

    <div class="event-date">
      <span class="day">7TH</span>
      <span class="month-year"><span class="month">AUGUST</span><span class="year">2021</span></span>
      <span class="divider"></span>
      <span class="time">11:00am-<br>to 2:00pm</span>
    </div>

    <p class="website">www.glimmerline-band.cpm</p>
  </main>
</body>
</html>
```